Seriöses Webdesign für innovatives Ingenieurbüro mit dem Schwerpunkt Eisenbahn Leit- und Sicherungstechnik
Zielgruppe
Die Webseite hat in erster Linie die Aufgabe zu informieren: An erster Stelle steht die Kontaktaufnahme und der Kompetenzbereich des Ingenieurbüros.
Folgende Kernkompetenzen sollen durch die Webseite transportiert werden:
Hardware-Entwicklung
Software-Entwicklung
Erneuerung alter Techniken
Begutachtung
Software für Lieferantenbewertung
Störungsmanagement(system)
Zielgruppe:
Die Webseite soll als Online-Visitenkarte für bestehende und neue Kontakte dienen. Gerade neue (Messe-)Kontakte erleben die Webseite als erste Anlaufstelle und erhalten einen Einblick in das vorhandene Leistungsspektrum des Ingenieurbüros und die Möglichkeiten der Kontaktaufnahme.

```html
<!DOCTYPE html>
<html lang="de">
<head>
<meta charset="utf-8">
<title>Velto Consult – Ingenieurbüro für Leit- und Sicherungstechnik</title>
<link href="https://fonts.googleapis.com/css2?family=Source+Sans+3:wght@400;600;700&display=swap" rel="stylesheet">
<style>
  :root{
    --sky:#7ac3e2;
    --sky-text:#5cb2dc;
    --ink:#2c3842;
    --ink-soft:#34424d;
    --text:#2a2a2a;
    --menu-bg:#e2f3fb;
    --band:#e3e3e3;
    --white:#ffffff;
  }
  *{margin:0;padding:0;box-sizing:border-box}
  html,body{width:922px;height:1200px;overflow:hidden}
  body{font-family:"Source Sans 3",sans-serif;color:var(--text);background:var(--white);position:relative}

  /* header */
  .site-header{position:absolute;left:0;top:0;width:922px;height:76px;background:var(--sky)}
  .brand{position:absolute;left:138px;top:20px;font-size:27px;font-weight:700;color:var(--white);letter-spacing:.3px}
  .lang{position:absolute;left:732px;top:30px;display:flex;gap:4px;font-size:8px;font-weight:700}
  .lang span{padding:3px 6px;color:var(--ink)}
  .lang .active{background:var(--white)}
  .lang .other{background:rgba(255,255,255,.45)}

  /* hero */
  .hero{position:absolute;left:0;top:77px;width:922px;height:270px;
    background:linear-gradient(180deg,#9aa6b2 0%,#b9c2ca 40%,#8e9083 72%,#7d8a5a 100%)}
  .service-menu{position:absolute;left:138px;top:117px;width:215px;height:143px;background:var(--menu-bg);
    border-radius:6px;padding:10px 14px;list-style:none}
  .service-menu li{font-size:10.5px;font-weight:600;color:var(--ink);height:21px;line-height:20px;padding-left:5px;
    border-bottom:1px solid var(--ink)}
  .service-menu li:last-child{border-bottom:none}
  .service-menu li.current{background:var(--ink);color:var(--white)}

  /* intro */
  .intro{position:absolute;left:0;top:349px;width:922px;height:241px;background:var(--ink);color:var(--white)}
  .intro h1{position:absolute;left:137px;top:27px;font-size:31px;font-weight:400;line-height:35px}
  .intro .route-art{position:absolute;left:305px;top:19px;width:225px;height:80px;background:var(--ink-soft);border-radius:2px}
  .intro .tagline{position:absolute;left:137px;top:105px;font-size:14.5px;font-weight:600;color:var(--sky-text)}
  .intro .lead{position:absolute;left:137px;top:150px;width:305px;font-size:11px;line-height:17px}
  .contact{position:absolute;left:597px;top:86px}
  .contact h2{font-size:23.5px;font-weight:700;color:var(--sky-text);line-height:26px}
  .contact .phone{font-size:10.5px;font-weight:700;margin-top:6px}
  .contact dt{font-size:10px;font-weight:700;color:var(--sky-text);margin-top:8px;line-height:12px}
  .contact dd{font-size:8.5px;font-weight:600;line-height:11px}

  /* features */
  .feature{position:absolute;top:623px;width:186px}
  .feature h3{display:flex;align-items:center;gap:12px;font-size:16px;font-weight:600;letter-spacing:.5px;color:var(--ink);height:46px}
  .feature .highlight{margin-top:18px;font-size:10.8px;line-height:15.4px;color:var(--sky-text)}
  .feature p{font-size:10.8px;line-height:15.4px}
  .feature .highlight + p{margin-top:15px}

  /* detail band */
  .detail{position:absolute;left:0;top:875px;width:922px;height:224px;background:var(--band)}
  .detail .pattern{position:absolute;inset:0;background:linear-gradient(180deg,#e6e6e6,#dfdfdf)}
  .detail .relays{position:absolute;left:166px;top:50px;width:150px;height:137px;
    background:linear-gradient(90deg,#b9b2a3 0%,#c9b998 40%,#e3e3e3 50%,#3b6b44 65%,#2f3a36 100%);border-radius:3px}
  .detail h2{position:absolute;left:382px;top:60px;font-size:24px;font-weight:700;line-height:29px;color:var(--ink)}
  .detail p{font-size:10.8px;line-height:15.4px;color:var(--text)}
  .detail .col-a{position:absolute;left:382px;top:127px;width:196px}
  .detail .col-b{position:absolute;left:604px;top:66px;width:196px}
  .detail .col-b p + p{margin-top:15px}

  /* footer */
  .site-footer{position:absolute;left:0;top:1101px;width:922px;height:99px;background:var(--sky);color:var(--ink)}
  .site-footer .brand-small{position:absolute;left:137px;top:28px;font-size:17px;font-weight:700;color:var(--white)}
  .site-footer .send{position:absolute;left:600px;top:37px;width:127px;height:24px;border:1px solid var(--white);
    color:var(--white);font-size:10.5px;font-weight:700;text-align:center;line-height:22px}
  .site-footer nav{position:absolute;left:137px;top:71px;font-size:9.5px;font-weight:600}
</style>
</head>
<body>

<header class="site-header">
  <div class="brand">Velto Consult</div>
  <div class="lang"><span class="active">DE</span><span class="other">ENG</span></div>
</header>

<section class="hero" role="img" aria-label="Foto: zwei Hochgeschwindigkeitszüge fahren aus einer Wartungshalle auf Gleise"></section>
<ul class="service-menu">
  <li>Hardware-Entwicklung</li>
  <li>Software-Entwicklung</li>
  <li class="current">Erneuerung alter Techniken</li>
  <li>Begutachtung</li>
  <li>Software für Lieferantenbewertung</li>
  <li>Störungsmanagement</li>
</ul>

<section class="intro">
  <h1>Wir stellen<br>Weichen</h1>
  <div class="route-art" role="img" aria-label="Illustration: gestrichelter Weg von einem Bildschirm zu einer Weichenanlage"></div>
  <div class="tagline">Maßgeschneiderte Softwarelösungen</div>
  <p class="lead">Hier sollte ein Text stehen, der uns zum Vorteil gereift. Hier sollte ein Text stehen, der uns zum Vorteil gereift. Hier sollte ein Text stehen, der uns zum Vorteil</p>
  <div class="contact">
    <h2>Kontakt zu uns</h2>
    <div class="phone">0 800 - 41 72 60 90</div>
    <dl>
      <dt>Montag – Donnerstag</dt>
      <dd>08:00 – 12:00 Uhr / 13:30 – 17:00 Uhr</dd>
      <dt>Freitag</dt>
      <dd>8:00 – 12:00 Uhr</dd>
    </dl>
  </div>
</section>

<article class="feature" style="left:137px">
  <h3>
    <svg width="34" height="32" viewBox="0 0 34 32">
      <rect x="1" y="1" width="32" height="13" fill="none" stroke="#2c3842" stroke-width="1.4"/>
      <circle cx="7" cy="15" r="3" fill="#2c3842"/><circle cx="17" cy="15" r="3" fill="#2c3842"/><circle cx="27" cy="21" r="3" fill="#2c3842"/>
      <path d="M2 30v-6a5 5 0 0 1 10 0v6zM12 30v-6a5 5 0 0 1 10 0v6zM22 30v-2a5 5 0 0 1 10 0v2z" fill="#2c3842"/>
    </svg>
    Schulungen
  </h3>
  <p class="highlight">Hier sollte ein Text stehen, der uns zum Vorteil gereift. Hier sollte ein Text stehen.</p>
  <p>Hier sollte ein Text stehen, der uns zum Vorteil gereift. Hier sollte ein Text stehen. Hier sollte ein Text stehen, der uns zum Vorteil gereift. Hier sollte ein Text stehen.</p>
</article>

<article class="feature" style="left:382px">
  <h3>
    <svg width="26" height="42" viewBox="0 0 26 42">
      <circle cx="9" cy="3" r="2" fill="#2c3842"/><circle cx="17" cy="3" r="2" fill="#2c3842"/>
      <rect x="1" y="7" width="24" height="28" rx="7" fill="#2c3842"/>
      <rect x="5" y="12" width="16" height="9" fill="#fff"/>
      <circle cx="7" cy="28" r="2" fill="#fff"/><circle cx="19" cy="28" r="2" fill="#fff"/>
      <path d="M5 35l-3 6M21 35l3 6" stroke="#2c3842" stroke-width="2.2"/>
    </svg>
    Spezialgebiete
  </h3>
  <p class="highlight">Hier sollte ein Text stehen, der uns zum Vorteil gereift. Hier sollte ein Text stehen. Hier sollte ein Text stehen.Hier sollte ein Text stehen.</p>
  <p>Hier sollte ein Text stehen, der uns zum Vorteil gereift. Hier sollte ein</p>
</article>

<article class="feature" style="left:602px">
  <h3>
    <svg width="20" height="20" viewBox="0 0 20 20">
      <path d="M10 1v9M5.5 6l4.5 4.5L14.5 6" fill="none" stroke="#2c3842" stroke-width="2.4"/>
      <rect x="7" y="0" width="6" height="3" fill="#2c3842"/>
      <path d="M1 12v7h18v-7" fill="none" stroke="#2c3842" stroke-width="2.4"/>
    </svg>
    Downloads
  </h3>
  <p style="margin-top:18px">Hier sollte ein Text stehen, der uns zum Vorteil gereift.</p>
</article>

<section class="detail">
  <div class="pattern" role="img" aria-label="Hintergrundgrafik: blasser Gleisplan eines Stellwerks"></div>
  <div class="relays" role="img" aria-label="Foto: zwei geöffnete Stellwerksrelais mit Spule und Platine"></div>
  <h2>In Kleinigkeiten<br>ganz groß</h2>
  <div class="col-a"><p>Hier sollte ein Text stehen, der uns zum Vorteil gereift. Hier sollte ein Text stehen, der uns zum Vorteil gereift.</p></div>
  <div class="col-b">
    <p>Hier sollte ein Text stehen, der uns zum Vorteil gereift. Hier sollte ein Text stehen, der uns zum Vorteil gereift.</p>
    <p>Hier sollte ein Text stehen, der uns zum Vorteil gereift. Hier sollte ein Text stehen, der uns zum Vorteil gereift.</p>
  </div>
</section>

<footer class="site-footer">
  <div class="brand-small">Velto</div>
  <div class="send">Nachricht senden &gt;&gt;</div>
  <nav>Startseite &nbsp;•&nbsp; AGB &nbsp;•&nbsp; Bankverbindung &nbsp;•&nbsp; Datenschutz &nbsp;•&nbsp; Impressum</nav>
</footer>

</body>
</html>
```